Business Card Design Project

I want a cleaner business card and envelope then what we have now, its too crowded.
Updates

I update with logo, this can be changed anyway you feel it looks best. I also have put gaurantee on there and extended time, this is my first time doing this. Also gave an example of current card

Target Market(s)

a wide array of customers from vantage 400 to small companies and cleints

Industry/Entity Type

Business

Requirements
Must have
• Need to have address, telephone number email
Nice to have
• a sharp professional card that stands out but is still very clean.
Should not have
• Not crazy looking

```html
<!DOCTYPE html>
<html lang="en">
<head>
<meta charset="utf-8">
<title>Halden Insurance Group — Stationery</title>
<link href="https://fonts.googleapis.com/css2?family=EB+Garamond:wght@400;500&display=swap" rel="stylesheet">
<style>
  :root{
    --backdrop:#e9e7e3;
    --paper-light:#f2f3f4;
    --paper-mid:#d9dbdd;
    --paper-edge:#c4c6c8;
    --ink:#5a5c5f;
    --ink-soft:#77797c;
    --card-dark:#3a3b3d;
    --card-dark-edge:#2c2d2e;
    --card-dark-ink:#e6e6e6;
    --card-dark-soft:#a9aaac;
    --mark:#6b6d70;
  }
  *{margin:0;padding:0;box-sizing:border-box}
  html,body{width:1200px;height:900px;overflow:hidden;background:var(--backdrop)}
  body{position:relative;font-family:"EB Garamond",Georgia,serif;color:var(--ink)}

  .paper{position:absolute;background:linear-gradient(160deg,var(--paper-light),var(--paper-mid));box-shadow:0 6px 18px rgba(0,0,0,.18)}

  /* envelope front */
  .envelope-front{left:60px;top:60px;width:640px;height:340px}
  .brand{position:absolute;display:flex;align-items:center;gap:12px}
  .brand-square{background:var(--mark)}
  .brand-name{font-weight:500;color:var(--mark);letter-spacing:.12em;text-transform:uppercase;line-height:1.05}
  .envelope-front .brand{left:44px;bottom:48px}
  .envelope-front .brand-square{width:38px;height:38px}
  .envelope-front .brand-name{font-size:19px}

  /* envelope back */
  .envelope-back{left:440px;top:480px;width:700px;height:320px;overflow:hidden}
  .envelope-flap{position:absolute;left:0;top:0;width:100%;height:150px}
  .envelope-address{position:absolute;right:26px;bottom:66px;font-size:12px;color:var(--ink-soft)}
  .envelope-phones{position:absolute;left:30px;bottom:24px;list-style:none;font-size:13px;line-height:1.45}
  .envelope-phones li{display:flex;align-items:center;gap:7px}
  .envelope-phones svg{width:13px;height:13px}

  /* business cards */
  .card{position:absolute;width:300px;height:170px;box-shadow:0 5px 14px rgba(0,0,0,.25)}
  .card-front{left:470px;top:400px;background:linear-gradient(160deg,var(--paper-light),var(--paper-mid))}
  .card-front .brand{left:50%;top:50%;transform:translate(-50%,-50%);flex-direction:column;gap:8px;text-align:center}
  .card-front .brand-square{width:30px;height:30px}
  .card-front .brand-name{font-size:15px}

  .card-back{left:790px;top:300px;background:var(--card-dark);border:1px solid var(--card-dark-edge);color:var(--card-dark-ink)}
  .card-person{position:absolute;left:22px;top:56px}
  .card-name{font-size:21px;font-weight:400}
  .card-title{font-size:8px;letter-spacing:.14em;text-transform:uppercase;color:var(--card-dark-soft);margin-top:2px}
  .card-street{position:absolute;left:22px;top:118px;font-size:7.5px;color:var(--card-dark-soft)}
  .card-divider{position:absolute;left:192px;top:46px;width:1px;height:64px;background:var(--card-dark-soft)}
  .card-contacts{position:absolute;left:202px;top:48px;list-style:none;font-size:7.5px;line-height:2;color:var(--card-dark-soft)}
  .card-contacts li{display:flex;align-items:center;gap:5px}
  .card-contacts i{width:6px;height:6px;background:var(--card-dark-soft);display:inline-block}
</style>
</head>
<body>

<section class="paper envelope-front" aria-label="Envelope front">
  <div class="brand">
    <span class="brand-square"></span>
    <span class="brand-name">Halden<br>Insurance Group</span>
  </div>
</section>

<section class="paper envelope-back" aria-label="Envelope back">
  <svg class="envelope-flap" viewBox="0 0 700 150" preserveAspectRatio="none" aria-hidden="true">
    <path d="M0 0 H700 V38 Q700 48 688 50 L360 118 Q350 120 340 118 L12 50 Q0 48 0 38 Z" fill="#cfd1d3" stroke="#b9bbbd" stroke-width="1"/>
  </svg>
  <p class="envelope-address">1180 Larkfield Ave, Cedar Point, MI 48000 www.haldengroup.com</p>
  <ul class="envelope-phones">
    <li><svg viewBox="0 0 16 16"><rect width="16" height="16" fill="#5a5c5f"/><path d="M4 3 L6.5 3 L7.5 6 L6 7 Q7 9.5 9 10 L10 8.5 L13 9.5 L13 12 Q8 13 4 8 Z" fill="#f2f3f4"/></svg>555-410-2200 ext 232</li>
    <li><svg viewBox="0 0 16 16"><rect width="16" height="16" fill="#5a5c5f"/><rect x="5" y="2.5" width="6" height="11" rx="1" fill="#f2f3f4"/><rect x="6" y="4" width="4" height="6" fill="#5a5c5f"/></svg>555-410-0138 (direct)</li>
    <li><svg viewBox="0 0 16 16"><rect width="16" height="16" fill="#5a5c5f"/><rect x="3" y="6" width="10" height="6" fill="#f2f3f4"/><rect x="5" y="3" width="6" height="3" fill="#f2f3f4"/></svg>555-410-2203</li>
  </ul>
</section>

<section class="card card-back" aria-label="Business card back">
  <div class="card-person">
    <p class="card-name">Marla Reese - Colton</p>
    <p class="card-title">Operation Manager</p>
  </div>
  <p class="card-street">1180 Larkfield Ave, Cedar Point, MI · www.haldengroup.com</p>
  <span class="card-divider"></span>
  <ul class="card-contacts">
    <li><i></i>555-410-2200 ext 232</li>
    <li><i></i>555-410-0138 direct</li>
    <li><i></i>555-410-2203</li>
    <li><i></i>mreese@haldengroup.com</li>
  </ul>
</section>

<section class="card card-front" aria-label="Business card front">
  <div class="brand">
    <span class="brand-square"></span>
    <span class="brand-name">Halden<br>Insurance Group</span>
  </div>
</section>

</body>
</html>
```